Business Card Design Project

Design business card based on logo provided.

Industry/Entity Type

Business

Requirements
Nice to have
• Logo to be provided.

Solid green second side with reverse logo (buildings only, not text).

Because the logo is linear I think that it might be possible to extend the logo lines across the card (only on the second side) as an interesting design element.

"Helping Owners Build Better Building Programs"

"Job Order Contracting and Best Value Specialist"

"Cooperation - Innovation - Efficiency"

Basic Info:
Nora Whitfield
Owner/Founder
505-718-6024
nora@norawhitfieldpartners.example

www.norawhitfieldpartners.example (this should probably be on reverse)

```html
<!DOCTYPE html>
<html lang="en">
<head>
<meta charset="utf-8">
<title>Nora Whitfield Partners — Business Card</title>
<link rel="stylesheet" href="https://fonts.googleapis.com/css2?family=Arimo:wght@400;700&display=swap">
<style>
  :root {
    --page: #ffffff;
    --ink: #111111;
    --olive: #4f5f2a;
    --leaf-light: #a9c43e;
    --leaf-mid: #7a9a31;
    --leaf-deep: #465f22;
    --card-border: #b5b5b5;
    --white: #ffffff;
  }
  * { box-sizing: border-box; margin: 0; padding: 0; }
  html, body {
    width: 1200px;
    height: 425px;
    overflow: hidden;
    background: var(--page);
    font-family: "Arimo", Arial, sans-serif;
  }
  .canvas {
    position: relative;
    width: 1200px;
    height: 425px;
  }
  .card {
    position: absolute;
    width: 513px;
    height: 292px;
  }
  .card--front {
    left: 73px;
    top: 69px;
    background: var(--white);
    border: 2px solid var(--card-border);
  }
  .card--back {
    left: 628px;
    top: 73px;
    background: linear-gradient(35deg, var(--leaf-deep) 0%, var(--leaf-mid) 50%, var(--leaf-light) 100%);
  }
  .brand {
    position: absolute;
    left: 18px;
    top: 80px;
    display: flex;
    align-items: center;
    gap: 10px;
  }
  .brand__mark {
    width: 18px;
    height: 18px;
    background: var(--leaf-mid);
  }
  .brand__name {
    font-size: 16px;
    font-weight: 700;
    letter-spacing: 0.3px;
    text-transform: uppercase;
    color: var(--olive);
  }
  .role {
    position: absolute;
    left: 336px;
    top: 64px;
    color: var(--olive);
    font-weight: 700;
  }
  .role__title { font-size: 19px; line-height: 24px; }
  .role__phone { font-size: 21px; line-height: 27px; letter-spacing: 0.5px; }
  .slogans {
    position: absolute;
    left: 0;
    right: 0;
    top: 126px;
    text-align: center;
    color: var(--ink);
    font-size: 17.5px;
    line-height: 23px;
  }
  .email {
    position: absolute;
    left: 0;
    right: 0;
    top: 248px;
    text-align: center;
    color: var(--olive);
    font-size: 18.5px;
    font-weight: 700;
  }
  .back-brand {
    position: absolute;
    left: 60px;
    right: 60px;
    top: 112px;
    display: flex;
    justify-content: center;
    align-items: center;
    gap: 14px;
  }
  .back-brand__mark {
    width: 26px;
    height: 26px;
    border: 4px solid var(--white);
  }
  .back-brand__name {
    color: var(--white);
    font-size: 24px;
    font-weight: 700;
    letter-spacing: 0.5px;
    text-transform: uppercase;
  }
  .website {
    position: absolute;
    left: 0;
    right: 0;
    top: 256px;
    text-align: center;
    color: var(--white);
    font-size: 18.5px;
    font-weight: 700;
  }
</style>
</head>
<body>
  <main class="canvas">
    <section class="card card--front" aria-label="Card front">
      <div class="brand">
        <span class="brand__mark" aria-hidden="true"></span>
        <span class="brand__name">Nora Whitfield Partners</span>
      </div>
      <div class="role">
        <p class="role__title">Owner/Founder</p>
        <p class="role__phone">505-718-6024</p>
      </div>
      <div class="slogans">
        <p>“Helping Owners Build Better Building Programs”</p>
        <p>“Job Order Contracting and Best Value Specialist”</p>
        <p>“Cooperation - Innovation - Efficiency”</p>
      </div>
      <p class="email">nora@norawhitfieldpartners.example</p>
    </section>

    <section class="card card--back" aria-label="Card back">
      <div class="back-brand">
        <span class="back-brand__mark" aria-hidden="true"></span>
        <span class="back-brand__name">Nora Whitfield Partners</span>
      </div>
      <p class="website">www.norawhitfieldpartners.example</p>
    </section>
  </main>
</body>
</html>
```